Internet Service Tech provider product flyer redesign - Skyloft Netlink

We have created the attached flyer in Word and also attached a PDF. All the content is correct. We just need a complete re-design of the flyer with new relevant hi-res images (based on content) and a more streamlined/cleaner layout.

This product is an entire in-building WIFI system for Body's Corporate in High Rise buildings.

We are a Brisbane-based internet tech company that specialises in providing solutions for High Rise buildings

Body text style - Helvetica Light

Internet

```html
<!DOCTYPE html>
<html lang="en">
<head>
<meta charset="utf-8">
<title>Skyloft Netlink – Flyer</title>
<link rel="stylesheet" href="https://fonts.googleapis.com/css2?family=Roboto:ital,wght@0,300;0,400;0,700;1,900&family=Roboto+Condensed:wght@700&display=swap">
<style>
  :root {
    --stage: #e4e4e4;
    --paper: #f4f4f4;
    --navy: #1b2350;
    --blue-deep: #1f2f7a;
    --blue-bright: #2f6fd0;
    --teal-band: #24546a;
    --red: #c8161d;
    --text-grey: #5a5a5a;
    --white: #ffffff;
  }
  html, body {
    margin: 0;
    width: 1200px;
    height: 900px;
    overflow: hidden;
    background: var(--stage);
  }
  .flyer {
    position: absolute;
    left: 320px;
    top: 50px;
    width: 560px;
    height: 800px;
    background: var(--paper);
    overflow: hidden;
    font-family: "Roboto", Helvetica, Arial, sans-serif;
    box-shadow: 0 6px 18px rgba(0,0,0,.18);
  }
  .flyer-shapes {
    position: absolute;
    inset: 0;
  }
  .headline {
    position: absolute;
    right: 26px;
    top: 56px;
    text-align: right;
    margin: 0;
    line-height: 1;
  }
  .headline-top {
    display: block;
    font-weight: 900;
    font-style: italic;
    font-size: 44px;
    color: var(--white);
    letter-spacing: -0.5px;
  }
  .headline-main {
    display: block;
    font-weight: 900;
    font-style: italic;
    font-size: 66px;
    color: var(--red);
    margin-top: 4px;
  }
  .headline-sub {
    display: block;
    font-weight: 700;
    font-size: 24px;
    color: var(--navy);
    margin-top: 4px;
  }
  .feature-label {
    position: absolute;
    top: 402px;
    width: 96px;
    height: 96px;
    display: flex;
    align-items: center;
    justify-content: center;
    text-align: center;
    font-family: "Roboto Condensed", "Arial Narrow", sans-serif;
    font-weight: 700;
    font-size: 16px;
    line-height: 1.1;
    color: var(--white);
    text-transform: uppercase;
  }
  .feature-text {
    position: absolute;
    top: 520px;
    width: 120px;
    margin: 0;
    text-align: center;
    font-weight: 300;
    font-size: 14px;
    line-height: 1.3;
    color: var(--text-grey);
  }
  .label-billing { left: 42px; }
  .label-wifi { left: 167px; }
  .label-supply { left: 292px; }
  .text-billing { left: 30px; }
  .text-wifi { left: 155px; }
  .text-supply { left: 280px; }
  .brand {
    position: absolute;
    left: 40px;
    bottom: 52px;
    margin: 0;
    font-weight: 700;
    font-size: 22px;
    color: var(--navy);
  }
</style>
</head>
<body>
<main class="flyer">
  <svg class="flyer-shapes" width="560" height="800" viewBox="0 0 560 800">
    <defs>
      <linearGradient id="cityGradient" x1="0" y1="1" x2="1" y2="0">
        <stop offset="0" stop-color="#8a1e2a"/>
        <stop offset="0.35" stop-color="#b23a55"/>
        <stop offset="0.65" stop-color="#3a3f8f"/>
        <stop offset="1" stop-color="#1a2a6a"/>
      </linearGradient>
      <linearGradient id="skyGradient" x1="0" y1="0" x2="1" y2="1">
        <stop offset="0" stop-color="#1d2463"/>
        <stop offset="0.6" stop-color="#2a5cb8"/>
        <stop offset="1" stop-color="#3b86e0"/>
      </linearGradient>
    </defs>
    <rect class="city-photo" x="0" y="0" width="560" height="450" fill="url(#cityGradient)" role="img" aria-label="Photo of city traffic light trails and towers at night"/>
    <path class="sky-panel" d="M300 0 C 320 200, 370 340, 470 440 L560 440 L560 0 Z" fill="url(#skyGradient)" role="img" aria-label="Photo of a glowing high-rise facade against a blue sky"/>
    <path d="M300 0 C 320 200, 370 340, 470 440" fill="none" stroke="#ffffff" stroke-width="8"/>
    <path class="lower-paper" d="M0 440 L560 440 L560 800 L0 800 Z" fill="#f4f4f4"/>
    <path class="navy-panel" d="M560 330 C 500 360, 470 400, 455 470 C 440 580, 450 700, 470 800 L560 800 Z" fill="#1b2350"/>
    <path d="M560 330 C 500 360, 470 400, 455 470" fill="none" stroke="#ffffff" stroke-width="8"/>
    <rect class="feature-band" x="0" y="440" width="460" height="20" fill="#24546a"/>
    <g class="feature-discs" fill="#c8161d" stroke="#ffffff" stroke-width="5">
      <circle cx="90" cy="450" r="48"/>
      <circle cx="215" cy="450" r="48"/>
      <circle cx="340" cy="450" r="48"/>
    </g>
    <g class="signal-badge">
      <circle cx="455" cy="450" r="46" fill="#ffffff"/>
      <g fill="none" stroke="#8a8a8a" stroke-width="3" stroke-linecap="round">
        <path d="M468 430 a20 20 0 0 1 0 28"/>
        <path d="M476 422 a32 32 0 0 1 0 44"/>
        <path d="M442 430 a20 20 0 0 0 0 28"/>
        <path d="M434 422 a32 32 0 0 0 0 44"/>
      </g>
      <g fill="none" stroke="#2f6fd0" stroke-width="2.5">
        <path d="M455 440 L442 480 M455 440 L468 480 M447 465 L463 465 M450 455 L460 455"/>
      </g>
      <circle cx="455" cy="440" r="4" fill="#2f6fd0"/>
    </g>
  </svg>

  <h1 class="headline">
    <span class="headline-top">Skyloft</span>
    <span class="headline-main">Netlink</span>
    <span class="headline-sub">for body's corporate</span>
  </h1>

  <div class="feature-label label-billing">Automated<br>Billing</div>
  <div class="feature-label label-wifi">HD WIFI</div>
  <div class="feature-label label-supply">Bulk<br>Supply</div>

  <p class="feature-text text-billing">and payment system that's simple, easy to use and available 24/7</p>
  <p class="feature-text text-wifi">designed specifically for high-rise buildings, using next-generation WIFI technology</p>
  <p class="feature-text text-supply">of Fibre-type Internet speeds delivered to all residents at wholesale prices</p>

  <p class="brand">Corvane Connect</p>
</main>
</body>
</html>
```